Past the Gravel

I need a book cover designed - 6 inches wide x 9 inches tall. I would like it Past the predominantly black and white, with a big bold title as attached:
Past the
GRAVEL
I have attached a black and white photo that I would like to cover the bottom half (or close to it) of the book, with the words: Life Lessons That Helped Build QTR, Pike B Dam, And Transform Loviter & BLUZ TV
By Gavin Melrose
The designs I've included here I don't particularly like, although I think you can see my general idea. He is a black and white man, so I have a back and white photo.
A big bold headline and not overly sized black and white

```html
<!DOCTYPE html>
<html lang="en">
<head>
<meta charset="utf-8">
<title>Past the Gravel — Book Cover</title>
<link rel="stylesheet" href="https://fonts.googleapis.com/css2?family=Anton&family=PT+Serif:wght@400&display=swap">
<style>
  :root {
    --cover-black: #000000;
    --ink-white: #ffffff;
    --photo-light: #6e6e6e;
    --photo-mid: #2a2a2a;
  }
  html, body {
    margin: 0;
    padding: 0;
    width: 800px;
    height: 1200px;
    overflow: hidden;
    background: var(--cover-black);
  }
  .cover {
    position: relative;
    width: 800px;
    height: 1200px;
    background: var(--cover-black);
    overflow: hidden;
  }
  .author-portrait {
    position: absolute;
    left: 390px;
    top: 617px;
    width: 410px;
    height: 583px;
    background: radial-gradient(ellipse at 45% 40%, var(--photo-light) 0%, var(--photo-mid) 45%, var(--cover-black) 80%);
  }
  .title {
    position: absolute;
    left: 0;
    top: 0;
    width: 800px;
    height: 620px;
  }
  .title text {
    font-family: "Anton", "Impact", sans-serif;
    fill: var(--ink-white);
  }
  .subtitle {
    position: absolute;
    left: 65px;
    top: 700px;
    margin: 0;
    font-family: "PT Serif", "Georgia", serif;
    font-weight: 400;
    font-size: 31px;
    line-height: 41px;
    color: var(--ink-white);
  }
  .divider {
    position: absolute;
    left: 65px;
    top: 1006px;
    width: 234px;
    height: 4px;
    background: var(--ink-white);
  }
  .byline {
    position: absolute;
    left: 65px;
    top: 1042px;
    margin: 0;
    font-family: "PT Serif", "Georgia", serif;
    font-size: 36px;
    line-height: 1;
    color: var(--ink-white);
  }
</style>
</head>
<body>
  <div class="cover">
    <div class="author-portrait" role="img" aria-label="Black and white profile photograph of the author facing left"></div>

    <svg class="title" viewBox="0 0 800 620" aria-label="Past the Gravel">
      <text class="title-line" x="86" y="289" font-size="300" textLength="621" lengthAdjust="spacingAndGlyphs">Past the</text>
      <text class="title-line title-line--main" x="58" y="578" font-size="300" textLength="692" lengthAdjust="spacingAndGlyphs">GRAVEL</text>
    </svg>

    <p class="subtitle">Life Lessons That<br>Helped Build QTR,<br>Pike B Dam,<br>And Transform<br>Loviter &amp;<br>BLUZ TV</p>

    <div class="divider"></div>

    <p class="byline">By Gavin Melrose</p>
  </div>
</body>
</html>
```